Larkfield Wp design

We need a wordpress design that will incorporate a professional color scheme with company logo in a clean layout. The design needs to consider that this will be developed on a responsive theme. Colors are undetermined - can use different blue or red as highlight - creative use of colors will be important. Client wants a 'modern' look.

Industry/Entity Type

It Company

Font styles to use
Serif
Sans Serif

Colors

Designer to choose colors to be used in the design.

Requirements
Must have
• - Navigation: 1) Home 2) Real Estate For Sale 3) Auctions 4) About Us 5) Selling Your Property 6) Contact Us

Site will have slideshow - 1st image is attached.
Home Page Content:
My service, experience and dedication provide motivated Sellers and Buyers with a clear marketing advantage. I know that the only way to succeed in real estate is to provide more service than you can get anywhere else. And you will get that kind of service when you work with me.
I will provide you with the personal service you deserve. Put my professional image, reputation, and business ethics to work for you.

Header will have - Logo (attached) Contact Information. 2 Real Estate listing buttons on the right for "New Listings" and "Upcoming Auctions" - similar to http://www.oakmereplots.example/home

and will have 4 call to action boxes- 1) Land 2) Residential 3) Commercial 4) Auctions

Footer will have site nav, smaller logo, and association logos (attached)
Nice to have
• use of dropdown menus

```html
<!DOCTYPE html>
<html lang="en">
<head>
<meta charset="utf-8">
<title>Larkfield Realty – Home</title>
<link href="https://fonts.googleapis.com/css2?family=Open+Sans:wght@400;600;700&display=swap" rel="stylesheet">
<style>
:root{
  --topbar:#5a1616;
  --navy:#2d2f63;
  --navy-dark:#22244d;
  --red:#7a1c1c;
  --ink:#333;
  --muted:#777;
  --line:#e2e2e2;
  --band:#1f2d38;
  --band-2:#2a3c49;
  --accent:#3a8fd8;
  --green:#5db043;
  --blue:#3a8fd8;
  --orange:#f07c2a;
  --footer:#303030;
  --footer-bottom:#232323;
  --white:#fff;
}
*{box-sizing:border-box;margin:0;padding:0}
html,body{width:1200px;height:2761px;overflow:hidden}
body{font-family:"Open Sans",Arial,sans-serif;color:var(--ink);background:#fff;font-size:10px;position:relative}
.wrap{position:absolute;left:305px;width:610px}
a{color:inherit;text-decoration:none}

/* top bar */
.topbar{position:absolute;top:0;left:0;width:1200px;height:32px;background:var(--topbar);color:#f1d9d9;font-size:9px}
.topbar .wrap{top:0;height:32px;display:flex;align-items:center;justify-content:space-between}
.topbar .links a{margin-right:12px}
.topbar .contact span{margin-left:14px}

/* header */
.header{position:absolute;top:32px;left:0;width:1200px;height:50px;background:#fff}
.brand{position:absolute;left:305px;top:6px;height:38px;display:flex;align-items:center;gap:8px}
.brand .mark{width:14px;height:14px;background:var(--red)}
.brand .name{font-size:20px;font-weight:700;color:var(--red)}
.nav{position:absolute;left:425px;top:0;height:50px;display:flex}
.nav a{display:flex;align-items:center;padding:0 11px;font-size:9.5px;font-weight:600;text-transform:uppercase;color:#444}
.nav a.active{background:#f2f2f2;border-top:3px solid var(--navy);color:var(--navy)}

/* hero */
.hero{position:absolute;top:82px;left:0;width:1200px;height:476px;background:linear-gradient(100deg,#d9d6d1 0%,#f4f3f0 35%,#e9e6e1 60%,#8d7e6f 85%,#6e6055 100%)}
.search{position:absolute;left:324px;top:160px;width:418px;background:var(--navy);color:#fff}
.search h3{font-size:14px;font-weight:600;padding:12px 14px 6px}
.search p{font-size:10px;font-weight:600;padding:0 14px 14px}
.search .row{display:flex;gap:6px;padding:12px 14px 16px;background:var(--navy-dark)}
.search .field{height:24px;background:#3a3c74;color:#cfd0e6;font-size:9px;display:flex;align-items:center;justify-content:space-between;padding:0 6px;flex:1}
.search .field::after{content:"▾";font-size:8px}
.search .go{width:26px;height:24px;background:#4a4c8c;display:flex;align-items:center;justify-content:center}

/* features */
.features{top:580px;display:flex;justify-content:space-between;padding:0 10px}
.feature{width:140px;display:flex;gap:8px}
.feature .ico{flex:none;width:24px;height:24px;border-radius:50%;background:var(--navy);display:flex;align-items:center;justify-content:center}
.feature h4{font-size:10px;font-weight:700;margin:2px 0 3px}
.feature p{font-size:8.5px;line-height:1.45;color:var(--muted)}

/* subscription */
.subscribe{top:715px;height:51px;background:var(--navy);color:#fff;display:flex;align-items:center;justify-content:space-between;padding:0 14px}
.subscribe h4{font-size:10px;font-weight:700}
.subscribe p{font-size:9px;margin-top:2px;color:#d6d7ee}
.btn-outline{border:1px solid #fff;padding:5px 10px;font-size:8.5px;font-weight:600;text-transform:uppercase}

/* section heading */
.sec-head{height:26px;border-bottom:2px solid var(--line);display:flex;justify-content:space-between;align-items:flex-start}
.sec-head h2{font-size:13px;font-weight:600;text-transform:uppercase;color:#222}
.arrows{display:flex;gap:2px}
.arrows span{width:16px;height:16px;background:#ddd;display:flex;align-items:center;justify-content:center;font-size:9px;color:#666}
.arrows span.on{background:#999;color:#fff}

/* property cards */
.cards{display:flex;justify-content:space-between;margin-top:14px}
.card{width:194px}
.card .photo{position:relative;height:127px}
.photo.home{background:linear-gradient(180deg,#9fc3e6 0%,#c9dde9 45%,#7aa05a 75%,#4f7a35 100%)}
.photo.office{background:linear-gradient(180deg,#f1f4f6 0%,#dfe5ea 55%,#8fb3cc 80%,#5d86a6 100%)}
.photo.pool{background:linear-gradient(180deg,#3d4f74 0%,#6b7ea6 40%,#c98a4f 70%,#3b6c8c 100%)}
.photo.family{background:linear-gradient(180deg,#c5d6e6 0%,#e3d3bd 50%,#b8926f 100%)}
.badge{position:absolute;right:0;font-size:8px;color:#fff;padding:2px 6px;font-weight:600}
.badge.top{top:4px}
.badge.low{top:20px}
.b-green{background:var(--green)}
.b-blue{background:var(--blue)}
.b-orange{background:var(--orange)}
.card h3{font-size:10.5px;font-weight:600;padding:9px 0 7px;border-bottom:1px solid var(--line)}
.card .specs{display:grid;grid-template-columns:1fr 1fr;font-size:8px;color:var(--muted);line-height:1.6;padding:7px 0;border-bottom:1px solid var(--line)}
.card .foot{display:flex;justify-content:space-between;align-items:center;padding-top:8px}
.card .price{font-size:10px;font-weight:600}
.btn{background:var(--navy);color:#fff;font-size:8px;font-weight:600;padding:5px 10px;text-transform:uppercase}

/* services band */
.band{position:absolute;top:1505px;left:0;width:1200px;height:226px;background:linear-gradient(160deg,var(--band-2) 0%,var(--band) 50%,#14202a 100%)}
.services{top:40px;display:grid;grid-template-columns:repeat(3,1fr);row-gap:36px;column-gap:18px;color:#cdd6dc}
.service{display:flex;gap:8px}
.service svg{flex:none}
.service h4{font-size:9.5px;font-weight:600;color:#fff;margin-bottom:4px}
.service p{font-size:8px;line-height:1.5;color:#9fb0bc}

/* testimonials & benefits */
.testi{top:1770px;width:285px}
.benefits{top:1770px;left:610px;width:305px}
.quote-row{display:flex;gap:14px;margin-top:18px}
.avatar{flex:none;width:62px;height:62px;border-radius:50%;background:linear-gradient(180deg,#c9ccd1,#8b8f96)}
.quote-mark{font-size:30px;color:#999;line-height:.8;font-family:Georgia,serif}
.quote-row p{font-size:8.5px;line-height:1.6;color:var(--muted)}
.author{text-align:right;font-size:8.5px;color:#555;margin-top:6px}
.dots{display:flex;gap:5px;justify-content:center;margin-top:10px;padding-left:70px}
.dots span{width:6px;height:6px;border-radius:50%;background:#bbb}
.dots span.on{background:#555}
.tabs{display:flex;margin-top:16px;border-bottom:1px solid var(--line)}
.tabs span{font-size:8.5px;padding:6px 10px;border:1px solid var(--line);border-bottom:none;margin-right:3px;background:#f6f6f6;color:#555}
.tabs span.on{background:#fff;color:#222;font-weight:600}
.panel{border:1px solid var(--line);border-top:none;padding:12px;font-size:8.5px;line-height:1.6;color:var(--muted);height:94px}

/* blog */
.blog{top:1990px}
.blog .sec-head h2{text-transform:none;font-size:14px}
.posts{display:flex;justify-content:space-between;margin-top:12px}
.post{width:296px}
.post .photo{position:relative;height:172px}
.photo.movers{background:linear-gradient(135deg,#f2f2f2 0%,#e8c9c2 45%,#c03a2e 70%,#f0e6d8 100%)}
.photo.plans{background:linear-gradient(135deg,#f4f6f8 0%,#dfe6ec 50%,#c0665a 78%,#e9ecef 100%)}
.date{position:absolute;top:6px;left:0;background:var(--navy);color:#fff;font-size:8px;padding:3px 8px;font-weight:600}
.tag{position:absolute;top:6px;left:96px;background:var(--navy-dark);color:#fff;font-size:8px;padding:3px 8px}
.post h3{font-size:11px;font-weight:600;margin-top:12px}
.post .meta{font-size:8px;color:#999;margin:4px 0 8px}
.post p{font-size:8.5px;line-height:1.6;color:var(--muted)}
.post .more{font-size:8.5px;color:#333;margin-top:4px}

/* partners */
.partners{top:2350px}
.partners h2{font-size:14px;font-weight:600;color:#222}
.partner-row{display:flex;justify-content:space-around;align-items:center;margin-top:24px;padding:0 30px}
.partner{background:#2a2a2a}

/* footer */
.footer{position:absolute;top:2500px;left:0;width:1200px;height:240px;background:var(--footer);color:#bbb}
.fcols{top:30px;display:flex;justify-content:space-between}
.fcol{width:140px}
.fcol h4{font-size:10px;font-weight:700;color:#fff;text-transform:uppercase;margin-bottom:12px}
.fprop{display:flex;gap:7px;margin-bottom:9px}
.fprop .thumb{flex:none;width:38px;height:28px;background:linear-gradient(180deg,#8fb0cf,#5d7e48)}
.fprop p{font-size:8.5px;color:#ddd;line-height:1.35}
.fprop small{display:block;font-size:7.5px;color:#999}
.gallery{display:grid;grid-template-columns:repeat(3,38px);gap:4px}
.gallery span{height:30px;background:linear-gradient(135deg,#7a5a4a,#b58d6b)}
.gallery span:nth-child(even){background:linear-gradient(135deg,#5d6f82,#9aa9b8)}
.cats li{list-style:none;font-size:8.5px;padding:3px 0;border-bottom:1px solid #3d3d3d}
.cats li::before{content:"›";margin-right:6px;color:#888}
.contact p{font-size:8.5px;line-height:1.6;margin-bottom:4px}
.social{display:flex;gap:5px;margin-top:8px}
.social span{width:14px;height:14px;border-radius:50%;background:#555}
.bottom{position:absolute;top:2740px;left:0;width:1200px;height:21px;background:var(--footer-bottom);color:#888;font-size:8px}
.bottom .wrap{top:0;height:21px;display:flex;align-items:center}
</style>
</head>
<body>

<div class="topbar">
  <div class="wrap">
    <div class="links"><a href="#">Terms &amp; Conditions</a><a href="#">Privacy Policy</a><a href="#">Membership</a></div>
    <div class="contact"><span>&#128100; Login</span><span>&#9742; (02) 5550 0142</span></div>
  </div>
</div>

<header class="header">
  <div class="brand"><span class="mark"></span><span class="name">Larkfield</span></div>
  <nav class="nav">
    <a href="#" class="active">Home</a>
    <a href="#">Real Estate For Sale</a>
    <a href="#">Auctions</a>
    <a href="#">About Us</a>
    <a href="#">Selling Your Property</a>
    <a href="#">Contact Us</a>
  </nav>
</header>

<section class="hero" role="img" aria-label="Bright modern living room with white sofa, shag rug, black armchair and stone fireplace">
  <form class="search">
    <h3>Find Property</h3>
    <p>Address, Suburbs, Postcodes, or Regions (separated by commas)</p>
    <div class="row">
      <span class="field">Location - any</span>
      <span class="field">Type</span>
      <span class="field">Beds</span>
      <span class="field">Max price</span>
      <span class="go"><svg width="11" height="11" viewBox="0 0 12 12"><circle cx="5" cy="5" r="3.5" fill="none" stroke="#fff" stroke-width="1.6"/><line x1="7.6" y1="7.6" x2="11" y2="11" stroke="#fff" stroke-width="1.6"/></svg></span>
    </div>
  </form>
</section>

<section class="wrap features">
  <div class="feature"><span class="ico"><svg width="11" height="11" viewBox="0 0 12 12"><path d="M1 10h10L6 3z" fill="#fff"/></svg></span><div><h4>Land</h4><p>Lorem ipsum dolor sit amet, consectetur adipiscing elit. Vivamus ac luctus ligula. Phasellus a ligula blandit.</p></div></div>
  <div class="feature"><span class="ico"><svg width="11" height="11" viewBox="0 0 12 12"><path d="M1 6L6 1l5 5v5H1z" fill="#fff"/></svg></span><div><h4>Residential</h4><p>Lorem ipsum dolor sit amet, consectetur adipiscing elit. Vivamus ac luctus ligula. Phasellus a ligula blandit.</p></div></div>
  <div class="feature"><span class="ico"><svg width="11" height="11" viewBox="0 0 12 12"><rect x="2" y="1" width="8" height="10" fill="#fff"/></svg></span><div><h4>Commercial</h4><p>Lorem ipsum dolor sit amet, consectetur adipiscing elit. Vivamus ac luctus ligula. Phasellus a ligula blandit.</p></div></div>
  <div class="feature"><span class="ico"><svg width="11" height="11" viewBox="0 0 12 12"><rect x="1" y="9" width="7" height="2" fill="#fff"/><rect x="4" y="2" width="6" height="3" fill="#fff" transform="rotate(35 7 3.5)"/></svg></span><div><h4>Auction</h4><p>Lorem ipsum dolor sit amet, consectetur adipiscing elit. Vivamus ac luctus ligula. Phasellus a ligula blandit.</p></div></div>
</section>

<section class="wrap subscribe">
  <div><h4>FREE SUBSCRIPTION</h4><p>You can submit you property per day</p></div>
  <a href="#" class="btn-outline">Register Now</a>
</section>

<section class="wrap" style="top:812px">
  <div class="sec-head"><h2>Properties For Sales</h2><div class="arrows"><span>&#8249;</span><span class="on">&#8250;</span></div></div>
  <div class="cards">
    <article class="card"><div class="photo home" role="img" aria-label="Farmhouse with green lawn"><span class="badge top b-green">Sale</span><span class="badge low b-blue">Office</span></div><h3>Central Park View</h3><div class="specs"><span>Area: 30000m2</span><span>Beds : 4 &nbsp; Baths : 3</span><span>Floors : 2 Garage : 1</span></div><div class="foot"><span class="price">$30000</span><a href="#" class="btn">View Details</a></div></article>
    <article class="card"><div class="photo office" role="img" aria-label="Open plan office interior"><span class="badge top b-green">Sale</span><span class="badge low b-blue">Commercial</span></div><h3>Central Park View</h3><div class="specs"><span>Area: 30000m2</span><span>Beds : 4 &nbsp; Baths : 3</span><span>Floors : 2 Garage : 1</span></div><div class="foot"><span class="price">$30000</span><a href="#" class="btn">View Details</a></div></article>
    <article class="card"><div class="photo office" role="img" aria-label="Open plan office interior"><span class="badge top b-green">Sale</span><span class="badge low b-blue">Commercial</span></div><h3>Central Park View</h3><div class="specs"><span>Area: 30000m2</span><span>Beds : 4 &nbsp; Baths : 3</span><span>Floors : 2 Garage : 1</span></div><div class="foot"><span class="price">$30000</span><a href="#" class="btn">View Details</a></div></article>
  </div>
</section>

<section class="wrap" style="top:1141px">
  <div class="sec-head"><h2>Properties For Rent</h2><div class="arrows"><span>&#8249;</span><span class="on">&#8250;</span></div></div>
  <div class="cards">
    <article class="card"><div class="photo family" role="img" aria-label="Suburban home with front garden"><span class="badge top b-orange">Rent</span><span class="badge low b-blue">Restaurant</span></div><h3>Central Park View</h3><div class="specs"><span>Area: 30000m2</span><span>Beds : 4 &nbsp; Baths : 3</span><span>Floors : 2 Garage : 1</span></div><div class="foot"><span class="price">$30000</span><a href="#" class="btn">View Details</a></div></article>
    <article class="card"><div class="photo pool" role="img" aria-label="Villa with pool at dusk"><span class="badge top b-orange">Rent</span><span class="badge low b-blue">Restaurant</span></div><h3>Central Park View</h3><div class="specs"><span>Area: 30000m2</span><span>Beds : 4 &nbsp; Baths : 3</span><span>Floors : 2 Garage : 1</span></div><div class="foot"><span class="price">$30000</span><a href="#" class="btn">View Details</a></div></article>
    <article class="card"><div class="photo family" role="img" aria-label="Suburban home with front garden"><span class="badge top b-orange">Rent</span><span class="badge low b-blue">Restaurant</span></div><h3>Central Park View</h3><div class="specs"><span>Area: 30000m2</span><span>Beds : 4 &nbsp; Baths : 3</span><span>Floors : 2 Garage : 1</span></div><div class="foot"><span class="price">$30000</span><a href="#" class="btn">View Details</a></div></article>
  </div>
</section>

<section class="band" role="img" aria-label="Dark textured water surface background">
  <div class="wrap services" style="left:315px;width:600px">
    <div class="service"><svg width="14" height="14" viewBox="0 0 14 14"><path d="M2 3l4 4-4 4M7 11h5" stroke="#3a8fd8" stroke-width="2" fill="none"/></svg><div><h4>Agency Leasing</h4><p>Lorem ipsum dolor sit amet, consectetur adipiscing elit. Vivamus ac luctus ligula. Phasellus a ligula blandit.</p></div></div>
    <div class="service"><svg width="14" height="14" viewBox="0 0 14 14"><path d="M1 7L7 1l6 6v6H1z" fill="#3a8fd8"/></svg><div><h4>Property and Asset Management</h4><p>Lorem ipsum dolor sit amet, consectetur adipiscing elit. Vivamus ac luctus ligula. Phasellus a ligula blandit.</p></div></div>
    <div class="service"><svg width="14" height="14" viewBox="0 0 14 14"><circle cx="7" cy="5" r="4" fill="#3a8fd8"/><rect x="5" y="10" width="4" height="3" fill="#3a8fd8"/></svg><div><h4>Real Estate Intelligence Service</h4><p>Lorem ipsum dolor sit amet, consectetur adipiscing elit. Vivamus ac luctus ligula. Phasellus a ligula blandit.</p></div></div>
    <div class="service"><svg width="14" height="14" viewBox="0 0 14 14"><path d="M2 2v5a5 5 0 0010 0V2h-3v5a2 2 0 01-4 0V2z" fill="#3a8fd8"/></svg><div><h4>Lease Administration</h4><p>Lorem ipsum dolor sit amet, consectetur adipiscing elit. Vivamus ac luctus ligula. Phasellus a ligula blandit.</p></div></div>
    <div class="service"><svg width="14" height="14" viewBox="0 0 14 14"><path d="M1 10l3-6 3 3 3-5 3 8z" fill="#3a8fd8"/></svg><div><h4>Transaction Management</h4><p>Lorem ipsum dolor sit amet, consectetur adipiscing elit. Vivamus ac luctus ligula. Phasellus a ligula blandit.</p></div></div>
    <div class="service"><svg width="14" height="14" viewBox="0 0 14 14"><path d="M7 1l5 4H2zM3 6h2v6H3zm3 0h2v6H6zm3 0h2v6H9z" fill="#3a8fd8"/></svg><div><h4>Strategic Consulting</h4><p>Lorem ipsum dolor sit amet, consectetur adipiscing elit. Vivamus ac luctus ligula. Phasellus a ligula blandit.</p></div></div>
  </div>
</section>

<section class="wrap testi">
  <div class="sec-head"><h2>Testimonials</h2></div>
  <div class="quote-row">
    <div class="avatar" role="img" aria-label="Client portrait"></div>
    <div><div class="quote-mark">&ldquo;</div><p>Nunc at pretium est curabitur, tempor vel lacus nec elementum egestas sed aliquet suspendisse. Lorem ipsum dolor sit amet consectetur adipiscing elit donec vel.</p><div class="author">- John Doe</div></div>
  </div>
  <div class="dots"><span class="on"></span><span></span></div>
</section>

<section class="wrap benefits">
  <div class="sec-head"><h2>Benefits From Property</h2></div>
  <div class="tabs"><span class="on">Unlimited Sites</span><span>Awesome UI</span><span>Elegant Design</span></div>
  <div class="panel">Lorem ipsum dolor sit amet, consectetur adipiscing elit. Fusce dapibus, tellus ac cursus commodo, tortor mauris condimentum nibh. Vestibulum id ligula porta felis euismod semper. Cras mattis consectetur purus sit amet fermentum.</div>
</section>

<section class="wrap blog">
  <div class="sec-head"><h2>From The Blog</h2><div class="arrows"><span>&#8249;</span><span class="on">&#8250;</span></div></div>
  <div class="posts">
    <article class="post"><div class="photo movers" role="img" aria-label="Couple moving boxes into a new home"><span class="date">November 17 2014</span><span class="tag">Featured</span></div><h3>Image - Minus id quod</h3><div class="meta">By creative design with &nbsp;| &nbsp;5 Comments</div><p>There are many variations of passages of Lorem Ipsum available, but the majority have suffered alteration in some form...</p><div class="more">More »</div></article>
    <article class="post"><div class="photo plans" role="img" aria-label="House model resting on building plans"><span class="date">November 17 2014</span></div><h3>Gallery - Cumque nihil impedit</h3><div class="meta">By creative design with &nbsp;| &nbsp;5 Comments</div><p>There are many variations of passages of Lorem Ipsum available, but the majority have suffered alteration in some form...</p><div class="more">More »</div></article>
  </div>
</section>

<section class="wrap partners">
  <h2>Our partners</h2>
  <div class="partner-row">
    <span class="partner" style="width:34px;height:28px" role="img" aria-label="Partner association badge"></span>
    <span class="partner" style="width:70px;height:20px;border-radius:10px" role="img" aria-label="Partner association badge"></span>
    <span class="partner" style="width:26px;height:28px" role="img" aria-label="Partner association badge"></span>
    <span class="partner" style="width:28px;height:28px;border-radius:50%" role="img" aria-label="Partner association badge"></span>
  </div>
</section>

<footer class="footer">
  <div class="wrap fcols">
    <div class="fcol"><h4>Properties</h4>
      <div class="fprop"><span class="thumb" role="img" aria-label="Property thumbnail"></span><p>Lorem ipsum dolor sit amet<small>$30,000</small></p></div>
      <div class="fprop"><span class="thumb" role="img" aria-label="Property thumbnail"></span><p>Lorem ipsum dolor sit amet<small>$30,000</small></p></div>
      <div class="fprop"><span class="thumb" role="img" aria-label="Property thumbnail"></span><p>Lorem ipsum dolor sit amet<small>$30,000</small></p></div>
    </div>
    <div class="fcol"><h4>Photos From Gallery</h4>
      <div class="gallery" role="img" aria-label="Grid of recent property photos"><span></span><span></span><span></span><span></span><span></span><span></span><span></span><span></span><span></span></div>
    </div>
    <div class="fcol"><h4>Categories</h4>
      <ul class="cats"><li>Apartment</li><li>Studio</li><li>Garage</li><li>Single Family</li><li>Condo</li><li>Land</li><li>Restaurant</li><li>Villas</li></ul>
    </div>
    <div class="fcol contact"><h4>Contact Info</h4>
      <p>14 Harrow Lane, Larkfield NSW 2100, Australia</p>
      <p>Phone: (02) 5550 0142</p>
      <p>Email: hello@larkfieldrealty.example</p>
      <p>Web: www.larkfieldrealty.example</p>
      <div class="social"><span></span><span></span><span></span><span></span><span></span></div>
    </div>
  </div>
</footer>
<div class="bottom"><div class="wrap">Copyright © 2014 Larkfield. All Rights Reserved.</div></div>

</body>
</html>
```